Millennial Survey Statistics Infogrpahic

We're a boutique creative consultancy specializing in informing Baby Boomers and Genreation X on how the millennial generation works, votes, and buys.

We recently conducted a survey amongst the millennial generation and we need to represent these stats in an infographic, that's visually interesting as well as concisely getting our information across to Boomers and Xer's.

We would like to see infographic designs that are split into three sections WORK, VOTE, and BUY with each section displaying its corresponding stats. We would also like to see designs that use our existing assets and style guide (Attached), as well as creating new assets as needed.

The Final design should communicate the stats in a visually appealing way to our target audience of baby boomers and generation x.

Target Market(s)

Generation X and Baby Boomers

Industry/Entity Type

Boutique

Requirements
Must have
• Use of our Style Guide approved colors, and fonts.

```html
<!DOCTYPE html>
<html lang="en">
<head>
<meta charset="utf-8">
<title>Buy — Millennial Survey Statistics</title>
<link href="https://fonts.googleapis.com/css2?family=Arimo:wght@400;700&display=swap" rel="stylesheet">
<style>
  :root {
    --bg: #ececec;
    --title: #8fb97c;
    --label: #7aa966;
    --callout-line: #b3b3b3;
    --green-1: #3f8a2f;
    --green-2: #55983f;
    --green-3: #6aa553;
    --green-4: #7fb267;
    --green-5: #4a9036;
    --hub: #ffffff;
    --hub-text: #8fb97c;
    --slice-text: #ffffff;
  }
  * { margin: 0; padding: 0; box-sizing: border-box; }
  html, body { width: 1200px; height: 1000px; overflow: hidden; }
  body {
    background: var(--bg);
    font-family: "Arimo", Arial, sans-serif;
    position: relative;
  }
  .section-title {
    position: absolute;
    left: 78px;
    top: 40px;
    font-size: 92px;
    font-weight: 700;
    letter-spacing: -6px;
    color: var(--title);
    line-height: 1;
  }
  .connectors { position: absolute; left: 0; top: 0; }
  .donut {
    position: absolute;
    width: 240px;
    height: 240px;
  }
  .donut svg { display: block; overflow: visible; }
  .donut .ring { fill: none; stroke-width: 32; }
  .donut .slice-label {
    fill: var(--slice-text);
    font-size: 10px;
    font-weight: 700;
    text-anchor: middle;
    dominant-baseline: middle;
  }
  .donut .hub-label {
    position: absolute;
    left: 50%;
    top: 50%;
    width: 112px;
    transform: translate(-50%, -50%);
    text-align: center;
    color: var(--hub-text);
    font-size: 14px;
    font-weight: 700;
    line-height: 1.15;
    text-transform: uppercase;
  }
  .callout {
    position: absolute;
    font-size: 9px;
    line-height: 1.3;
    color: var(--label);
    width: 165px;
  }
  .callout h2 {
    font-size: 9px;
    font-weight: 700;
    text-transform: uppercase;
  }
  .callout p { font-weight: 400; }
</style>
</head>
<body>
  <h1 class="section-title">BUY</h1>

  <svg class="connectors" width="1200" height="1000" aria-hidden="true">
    <g fill="none" stroke="var(--callout-line)" stroke-width="1">
      <polyline points="150,392 150,325 270,325"/>
      <polyline points="505,392 505,330 600,330"/>
      <polyline points="855,392 855,330 950,330"/>
      <polyline points="160,742 160,700 265,700"/>
      <polyline points="850,737 850,695 945,695"/>
    </g>
    <g fill="#fff" stroke="var(--green-5)" stroke-width="3">
      <circle cx="275" cy="325" r="4"/>
      <circle cx="605" cy="330" r="4"/>
      <circle cx="955" cy="330" r="4"/>
      <circle cx="270" cy="700" r="4"/>
      <circle cx="950" cy="695" r="4"/>
    </g>
  </svg>

  <svg width="0" height="0" style="position:absolute">
    <defs>
      <filter id="hub-shadow" x="-30%" y="-30%" width="160%" height="160%">
        <feDropShadow dx="0" dy="3" stdDeviation="4" flood-color="#000" flood-opacity="0.3"/>
      </filter>
    </defs>
  </svg>

  <!-- Technology used for shopping online -->
  <div class="donut donut-technology" style="left:30px; top:360px;">
    <svg width="240" height="240" viewBox="-120 -120 240 240">
      <g transform="rotate(-90)">
        <circle class="ring" r="72" pathLength="360" stroke="var(--green-4)" stroke-dasharray="40 360" stroke-dashoffset="0"/>
        <circle class="ring" r="72" pathLength="360" stroke="var(--green-1)" stroke-dasharray="40 360" stroke-dashoffset="-40"/>
        <circle class="ring" r="72" pathLength="360" stroke="var(--green-3)" stroke-dasharray="25 360" stroke-dashoffset="-80"/>
        <circle class="ring" r="72" pathLength="360" stroke="var(--green-2)" stroke-dasharray="45 360" stroke-dashoffset="-105"/>
        <circle class="ring" r="72" pathLength="360" stroke="var(--green-5)" stroke-dasharray="210 360" stroke-dashoffset="-150"/>
      </g>
      <circle r="57" fill="var(--hub)" filter="url(#hub-shadow)"/>
      <text class="slice-label" x="25" y="-68">36.8 %</text>
      <text class="slice-label" x="64" y="-36">34 %</text>
      <text class="slice-label" x="70" y="3">16.2%</text>
      <text class="slice-label" x="57" y="43">12%</text>
      <text class="slice-label" x="-72" y="-19">80%</text>
    </svg>
    <div class="hub-label">Techno&shy;logy used for shopping online</div>
  </div>
  <div class="callout" style="left:290px; top:312px;">
    <h2>What technology they use when shopping online</h2>
    <p>Mobile Device/Smartphone 36.8%<br>Laptop 34%<br>Desktop Computer 16.2%<br>Tablet 12%<br>80% of Millennials have used their mobile phone in a store to compare prices online.</p>
  </div>

  <!-- Most important to millennial shoppers -->
  <div class="donut donut-priorities" style="left:385px; top:360px;">
    <svg width="240" height="240" viewBox="-120 -120 240 240">
      <g transform="rotate(-90)">
        <circle class="ring" r="72" pathLength="94.5" stroke="var(--green-3)" stroke-dasharray="45.4 94.5" stroke-dashoffset="0"/>
        <circle class="ring" r="72" pathLength="94.5" stroke="var(--green-1)" stroke-dasharray="43.3 94.5" stroke-dashoffset="-45.4"/>
        <circle class="ring" r="72" pathLength="94.5" stroke="var(--green-2)" stroke-dasharray="5.8 94.5" stroke-dashoffset="-88.7"/>
      </g>
      <circle r="57" fill="var(--hub)" filter="url(#hub-shadow)"/>
      <text class="slice-label" x="72" y="5">45.4 %</text>
      <text class="slice-label" x="-69" y="20">43.3 %</text>
      <text class="slice-label" x="-18" y="-70">5.8 %</text>
    </svg>
    <div class="hub-label">Most important to millenial shoppers</div>
  </div>
  <div class="callout" style="left:620px; top:318px;">
    <h2>What is most important to millennial shoppers?</h2>
    <p>Quality 45.4%<br>Price 43.3%<br>Purpose or Mission 5.8%</p>
  </div>

  <!-- Preferred shopping referrals -->
  <div class="donut donut-referrals" style="left:735px; top:360px;">
    <svg width="240" height="240" viewBox="-120 -120 240 240">
      <g transform="rotate(-90)">
        <circle class="ring" r="72" pathLength="96.8" stroke="var(--green-5)" stroke-dasharray="54 96.8" stroke-dashoffset="0"/>
        <circle class="ring" r="72" pathLength="96.8" stroke="var(--green-4)" stroke-dasharray="24.8 96.8" stroke-dashoffset="-54"/>
        <circle class="ring" r="72" pathLength="96.8" stroke="var(--green-3)" stroke-dasharray="13.6 96.8" stroke-dashoffset="-78.8"/>
        <circle class="ring" r="72" pathLength="96.8" stroke="var(--green-1)" stroke-dasharray="4.4 96.8" stroke-dashoffset="-92.4"/>
      </g>
      <circle r="57" fill="var(--hub)" filter="url(#hub-shadow)"/>
      <text class="slice-label" x="70" y="20">54%</text>
      <text class="slice-label" x="-66" y="28">24.8%</text>
      <text class="slice-label" x="-50" y="-50">13.6%</text>
      <text class="slice-label" x="-12" y="-71">4.4%</text>
    </svg>
    <div class="hub-label">Preferred shopping referrals</div>
  </div>
  <div class="callout" style="left:970px; top:318px;">
    <h2>Preferred shopping referrals</h2>
    <p>Product Review Sites 54%<br>Friends and Family 24.8%<br>Company Website 13.6%<br>Company Social Media Site 4.4%</p>
  </div>

  <!-- What they rather own or share -->
  <div class="donut donut-own-share" style="left:40px; top:710px;">
    <svg width="240" height="240" viewBox="-120 -120 240 240">
      <g transform="rotate(-90)">
        <circle class="ring" r="72" pathLength="96" stroke="var(--green-4)" stroke-dasharray="53 96" stroke-dashoffset="0"/>
        <circle class="ring" r="72" pathLength="96" stroke="var(--green-1)" stroke-dasharray="43 96" stroke-dashoffset="-53"/>
      </g>
      <circle r="57" fill="var(--hub)" filter="url(#hub-shadow)"/>
      <text class="slice-label" x="60" y="48">53 %</text>
      <text class="slice-label" x="-71" y="-11">43 %</text>
    </svg>
    <div class="hub-label">What they rather own or share</div>
  </div>
  <div class="callout" style="left:285px; top:688px;">
    <h2>Would they rather own or share?</h2>
    <p>Sharing/ Having access to certain products 57%<br>Owning certain products 43%</p>
  </div>

  <!-- Consumer debt -->
  <div class="donut donut-debt" style="left:730px; top:710px;">
    <svg width="240" height="240" viewBox="-120 -120 240 240">
      <g transform="rotate(-90)">
        <circle class="ring" r="72" pathLength="132.2" stroke="var(--green-3)" stroke-dasharray="45.4 132.2" stroke-dashoffset="0"/>
        <circle class="ring" r="72" pathLength="132.2" stroke="var(--green-5)" stroke-dasharray="42.4 132.2" stroke-dashoffset="-45.4"/>
        <circle class="ring" r="72" pathLength="132.2" stroke="var(--green-4)" stroke-dasharray="30.6 132.2" stroke-dashoffset="-87.8"/>
        <circle class="ring" r="72" pathLength="132.2" stroke="var(--green-1)" stroke-dasharray="13.8 132.2" stroke-dashoffset="-118.4"/>
      </g>
      <circle r="57" fill="var(--hub)" filter="url(#hub-shadow)"/>
      <text class="slice-label" x="70" y="8">45.4 %</text>
      <text class="slice-label" x="-20" y="70">42.4%</text>
      <text class="slice-label" x="-71" y="-14">30.6%</text>
      <text class="slice-label" x="-24" y="-68">13.8%</text>
    </svg>
    <div class="hub-label">Consumer debt</div>
  </div>
  <div class="callout" style="left:965px; top:683px;">
    <h2 style="text-transform:none">Consumer Debt</h2>
    <p>Credit Cars 45.4%<br>Student Loans 42.4%<br>Car Loan 30.6%<br>Mortgage 13.8%</p>
  </div>
</body>
</html>
```